Commercial Real Estate

We need a business card design for a new commercial real estate business that specializes in apartment building brokerage. Not individual units but the entire complex. We find and represent the owners existing buildings and well as new buyers for those buildings. The design should convey trust, integrity, knowledge and growth. It should be easily read.

Target Market(s)

40 to 65 years old

Industry/Entity Type

Real Estate

```html
<!DOCTYPE html>
<html lang="en">
<head>
<meta charset="utf-8">
<title>Talloak Property Investments – Business Card</title>
<link href="https://fonts.googleapis.com/css2?family=Jura:wght@400;600;700&display=swap" rel="stylesheet">
<style>
  :root{
    --stage:#2e2f31;
    --teal:#5ec8c3;
    --teal-light:#8fdcd8;
    --slate:#4e5f5e;
    --paper:#ffffff;
    --paper-shade:#e6e8e8;
    --ink-white:#ffffff;
    --ink-dark:#3f4b4b;
  }
  *{box-sizing:border-box;margin:0;padding:0}
  html,body{width:1200px;height:892px;overflow:hidden;background:var(--stage)}
  body{font-family:"Jura",sans-serif;position:relative}

  .card{position:absolute;width:620px;height:354px;border-radius:4px;overflow:hidden;
        box-shadow:0 10px 30px rgba(0,0,0,.45)}
  .card--front{left:290px;top:52px;background:var(--teal)}
  .card--back{left:290px;top:486px;background:var(--paper)}

  /* front */
  .front-panel{position:absolute;left:0;top:0;right:0;bottom:62px;
               background:linear-gradient(160deg,var(--paper) 20%,var(--paper-shade) 100%);
               display:flex;flex-direction:column;align-items:center;justify-content:center;gap:8px}
  .brand-name{font-weight:700;font-size:46px;letter-spacing:4px;color:var(--slate);
              display:flex;align-items:center;gap:14px}
  .brand-mark{width:22px;height:22px;background:var(--teal)}
  .brand-tagline{font-weight:700;font-size:17px;letter-spacing:3px;color:var(--slate)}
  .front-url{position:absolute;left:30px;bottom:20px;color:var(--ink-white);
             font-size:17px;letter-spacing:2px}

  /* back */
  .back-brand{position:absolute;right:34px;top:26px;text-align:right}
  .back-brand .brand-name{font-size:30px;letter-spacing:3px;justify-content:flex-end;gap:10px}
  .back-brand .brand-mark{width:14px;height:14px}
  .back-brand .brand-tagline{font-size:12px;letter-spacing:2px;margin-top:2px}

  .details{position:absolute;left:0;top:108px;display:flex;flex-direction:column;gap:10px}
  .row{display:flex;align-items:center;height:48px;border-radius:0 10px 10px 0;
       background:var(--teal);color:var(--ink-white);font-size:15px;letter-spacing:1.5px}
  .row-icon{width:48px;height:100%;display:flex;align-items:center;justify-content:center;
            background:var(--teal-light)}
  .row-icon svg{width:20px;height:20px}
  .row-text{padding:0 18px;line-height:1.25}
  .row--name{background:var(--slate);width:330px;height:62px;border-radius:0 12px 12px 0;
             padding-left:48px;flex-direction:column;align-items:flex-start;justify-content:center}
  .person-name{font-size:26px;font-weight:600;letter-spacing:3px}
  .person-title{font-size:12px;letter-spacing:2.5px;margin-top:2px}
  .row--address{width:470px}
  .row--phone{width:420px}
  .row--web{width:560px;height:56px}
</style>
</head>
<body>

<section class="card card--front" aria-label="Card front">
  <div class="front-panel">
    <div class="brand-name"><span class="brand-mark"></span>TALLOAK</div>
    <div class="brand-tagline">Property Investments</div>
  </div>
  <p class="front-url">www.talloakpi.com</p>
</section>

<section class="card card--back" aria-label="Card back">
  <div class="back-brand">
    <div class="brand-name"><span class="brand-mark"></span>TALLOAK</div>
    <div class="brand-tagline">Property Investments</div>
  </div>

  <div class="details">
    <div class="row row--name">
      <div class="person-name">DANIEL REYES</div>
      <div class="person-title">GENERAL MANAGER</div>
    </div>
    <div class="row row--address">
      <span class="row-icon"><svg viewBox="0 0 20 20"><path d="M2 10 L10 3 L18 10 M5 8 V17 H15 V8" fill="none" stroke="#fff" stroke-width="2" stroke-linejoin="round"/></svg></span>
      <span class="row-text">45 Harbor Road, 2nd building Street E.</span>
    </div>
    <div class="row row--phone">
      <span class="row-icon"><svg viewBox="0 0 20 20"><path d="M5 2 H8 L9 6 L7 8 Q9 12 12 13 L14 11 L18 12 V15 Q18 18 15 18 Q3 16 2 5 Q2 2 5 2Z" fill="#fff"/></svg></span>
      <span class="row-text">014 220 3158</span>
    </div>
    <div class="row row--web">
      <span class="row-icon"><svg viewBox="0 0 20 20"><rect x="2" y="4" width="16" height="12" rx="1" fill="none" stroke="#fff" stroke-width="2"/><path d="M2 5 L10 11 L18 5" fill="none" stroke="#fff" stroke-width="2"/></svg></span>
      <span class="row-text">hello@talloakpi.com<br>www.talloakpi.com</span>
    </div>
  </div>
</section>

</body>
</html>
```